■依頼の目的/概要
販売予定しているオリジナル保湿美容液の「ふわりん艶雫」のラベルデザインをお願いします。

■依頼詳細
今回は、web通販限定で販売予定の乾燥肌に悩むにアラサー女性のための保湿美容液に貼り付けるラベルデザインの依頼です。
容器は、50ml入り乳白色のポンプ式プラスチックボトルです。

【企業理念、ビジョン】
素肌を美しくすることで、自分に自信が持てない女性を、未来に向かって明るく生きる輝く女性へと変身させ、幸せな女性を増やすことを理念・ビジョンとしています。

【商品コンセプト】
ブランドオーナー自身が、乾燥によある肌トラブル(赤ら顔、かゆみ)に悩まされていました。皮膚科医に「体質だからしょうがない」と治療してもらえず、諦めていました。
しかし、恩人から保湿をしっかりするようにとアドバイスをもらい、保湿をするようになってから劇的に改善し、今では「肌がきれい」と周りに褒めれるようになりました。この経験から、同じ悩みを持つ女性が一人でも多く美しい肌を手に入れ、自信を取り戻し、イキイキと輝いてほしいという願いを込めて、開発した美容液です。
薬剤師であるブランドオーナーがその知識を活かして漢方生薬や植物性成分を配合した安全安心の自然派の保湿美容液です。

■商品名
ふわりん艶雫

■サイズやファイル形式
容器表面のデザインをお願いします。
タテ6cm×ヨコ5cm以内のデザイン
イラストレーターでバージョン:cs4以下
アウトライン:有り/無し共にお願いします。

■その他要望
シンプルの中に高級感があるものを希望しています。
シンプル、自然派スキンケア、潤いをイメージできるものを希望します。
7000〜9000円の比較的高価格帯での販売予定ですので、
安っぽい感じにならないようお願いします。

選択させて頂いたデザインの著作権(財産権)等の扱いはKreavo利用規約に従い、弊社に譲渡をお願いします。フォントや画像素材などを利用する場合は上記利用用途に使用できることを確認し、第三者の知的財産権等に注意して下さい。

加筆や修正することがありますのでご了承くださいませ

その他何かご不明な点がございましたら、お気軽にご質問下さい。
よろしくお願いいたします。

商品コンセプトを元に、ターゲットとなる女性や知人、友人、ビジネスパートナーと意見交換をして決定しました。
当選のクレアボーさんには、修正を何度もしていただき感謝しております。

たくさんの提案をいただきありがとうございました!
素敵な提案が多く、選定にかなり悩みました。
クレアボの利用が初めてで不安も多かっですが、
無事オリジナルラベルができうれしく思っています。
本当にありがとうございました!

```html
<!DOCTYPE html>
<html lang="ja">
<head>
<meta charset="utf-8">
<title>ふわりん艶雫 ラベル</title>
<link rel="stylesheet" href="https://fonts.googleapis.com/css2?family=Noto+Serif+JP:wght@400;600&display=swap">
<style>
  :root {
    --page-bg: #ecebe9;
    --label-pink: #f6e7e4;
    --panel-pink: #fcf1ef;
    --navy: #1f2b63;
    --drop-light: #6d86c8;
    --drop-dark: #1d3a87;
  }
  html, body {
    margin: 0;
    padding: 0;
    width: 676px;
    height: 1200px;
    overflow: hidden;
    background: var(--page-bg);
  }
  .canvas {
    position: relative;
    width: 676px;
    height: 1200px;
  }
  .label {
    position: absolute;
    left: 97px;
    top: 0;
    width: 482px;
    height: 1200px;
    overflow: hidden;
  }
  .label-pattern {
    position: absolute;
    inset: 0;
    background: linear-gradient(180deg, #f8eae7 0%, var(--label-pink) 50%, #f4e3e0 100%);
  }
  .label-art {
    position: absolute;
    inset: 0;
  }
  .product-name {
    position: absolute;
    writing-mode: vertical-rl;
    font-family: "Noto Serif JP", serif;
    font-weight: 600;
    font-size: 95px;
    line-height: 1;
    letter-spacing: 0.02em;
    color: var(--navy);
  }
  .name-first {
    left: 280px;
    top: 420px;
  }
  .name-second {
    left: 190px;
    top: 482px;
  }
  .category {
    position: absolute;
    left: 0;
    width: 482px;
    top: 936px;
    text-align: center;
    font-family: "Noto Serif JP", serif;
    font-weight: 400;
    font-size: 32px;
    letter-spacing: 0.06em;
    color: #3a3a46;
  }
</style>
</head>
<body>
  <div class="canvas">
    <div class="label">
      <div class="label-pattern" role="img" aria-label="白い草花模様が散る淡いピンクの地紋"></div>

      <svg class="label-art" width="482" height="1200" viewBox="0 0 482 1200" aria-hidden="true">
        <defs>
          <linearGradient id="dropFill" x1="0" y1="0" x2="1" y2="1">
            <stop offset="0" stop-color="var(--drop-light)"/>
            <stop offset="1" stop-color="var(--drop-dark)"/>
          </linearGradient>
        </defs>
        <rect class="band" x="0" y="439" width="482" height="59" fill="var(--navy)"/>
        <path class="frame"
              d="M150,382 H370 A20 20 0 0 0 390 402 V892 A20 20 0 0 0 370 912 H150 A20 20 0 0 0 130 892 V402 A20 20 0 0 0 150 382 Z"
              fill="var(--panel-pink)" stroke="var(--navy)" stroke-width="4"/>
        <path class="frame-inner"
              d="M156,392 H364 A16 16 0 0 0 380 408 V886 A16 16 0 0 0 364 902 H156 A16 16 0 0 0 140 886 V408 A16 16 0 0 0 156 392 Z"
              fill="none" stroke="var(--navy)" stroke-width="1.5"/>
        <path class="drop"
              d="M303,305 C303,305 269,352 269,384 A34 34 0 0 0 337 384 C337,352 303,305 303,305 Z"
              fill="url(#dropFill)"/>
      </svg>

      <div class="product-name name-first">ふわりん</div>
      <div class="product-name name-second">艶雫</div>
      <div class="category">保湿美容液</div>
    </div>
  </div>
</body>
</html>
```